依頼詳細
いまあるサンプルを春らしく変えて頂いても結構ですし、違うイメージで一から作成して頂いても結構です。このサンプルデザインに特にこだわりがあるわけではありませんので、良いデザインがあればどんどんご提案下さい。

対象が女性の50代~70代になるのでデザインのおしゃれさも大事ですが、シンプルでわかりやすいデザインを希望します。

A3サイズとB4サイズで作成をして下さい。
内容はまったく同じで用紙に合わせてレイアウトを調整して下さい。

真ん中部分の広告商品の商品名や価格はダミーで入れて頂ければ後から私が加筆します。

今後は季節ごとに配色を変えたり、季節感のある物を軽く挿入する程度で、作って頂いたデザインを通年使用していく予定です。

2ヶ月ごとに新聞広告の作成がありますので、今後ともよろしくお願いします。

選択させて頂いた広告の著作権(財産権)等は当方に譲渡をお願いします。フォントや画像素材などを利用する場合は上記利用用途に使用できることを確認し、第三者の知的財産権等に注意して下さい。
記載項目
会期 4月5日(火)~10日(日)

営業時間 10:00~18:00(最終日のみ15:00迄)

会場 アサギリモール一階・北側 SPACEはなゆき 京都市北区雲井南梅枝町38-6

主催 株式会社明葉 京都市北区雲井西竹丘町17-42 tel075-555-0183

2015年4月のサンプルにあるネットショップとブログの案内は省いて下さい。
サイズ
A3
ページ数
片面
希望イメージ
シンプル 複雑
単色 カラフル
暗い 明るい
日常 高級
遊び心 厳粛
未来的 伝統的
女性的 男性的
希望する色
納品ファイル
• 高解像度JPG (.jpg)
• イラストレーター形式 (.ai)
• フォトショップ形式 (.psd)
補足説明
サンプルを添付をさせて頂きます
たくさんのすばらしいデザインを作成して頂き、皆様本当にありがとうございます。

良いデザインばかりなので選定作業が困難を極めています(笑)

採用させて頂いた方はもちろん、それ以外の方も今後ともよろしくお願い申し上げます。

ありがとうございました。
■ 選んだ理由

女性のデザイナーさんらしくやさしさが伝わってきました。

■ 提案者全員のお礼・コメント

皆様本当にありがとうございました。明葉の広告をこんなたくさんの方にデザインしていただきうれしく思います。今後もよろしくお願いします。

```html
<!DOCTYPE html>
<html lang="ja">
<head>
<meta charset="utf-8">
<title>明葉の婦人服 春祭り</title>
<link href="https://fonts.googleapis.com/css2?family=Noto+Sans+JP:wght@500;700;900&family=Shippori+Mincho+B1:wght@700;800&family=Yuji+Syuku&display=swap" rel="stylesheet">
<style>
:root{
  --magenta:#c8236e;
  --magenta-deep:#8e0f4c;
  --pink-light:#f6b7d2;
  --pink-pale:#fde6ef;
  --gold-1:#fff3b0;
  --gold-2:#f4c542;
  --gold-3:#c98a12;
  --cream:#fff9e4;
  --ink:#4a2a35;
  --white:#ffffff;
}
*{margin:0;padding:0;box-sizing:border-box}
html,body{width:843px;height:1200px;overflow:hidden;background:#fff}
.poster{position:relative;width:843px;height:1200px;overflow:hidden;font-family:"Noto Sans JP",sans-serif;
  background:linear-gradient(180deg,#f7a8cb 0%,var(--magenta) 22%,var(--magenta-deep) 38%,var(--magenta) 48%,#fff 56%,#fff 78%,var(--pink-pale) 100%)}
.flower-deco{position:absolute;border-radius:50%;background:radial-gradient(circle,#ffd6e8 0%,rgba(255,180,210,.35) 60%,rgba(255,180,210,0) 100%)}
.flower-deco.left{left:-40px;top:-40px;width:260px;height:200px}
.flower-deco.right{left:560px;top:-30px;width:200px;height:170px}
.brand{position:absolute;right:6px;top:0;width:122px;height:84px;background:var(--magenta-deep);color:var(--white);
  text-align:center;padding-top:18px}
.brand .name{font-weight:700;font-size:20px;letter-spacing:2px}
.brand .sub{font-weight:500;font-size:11px;margin-top:4px}
.sale-band{position:absolute;left:379px;top:0;width:84px;height:345px;background:linear-gradient(180deg,var(--cream),#ffe9a8);
  display:flex;flex-direction:row-reverse;align-items:center;justify-content:center;gap:4px;
  box-shadow:0 2px 8px rgba(0,0,0,.2)}
.sale-band span{writing-mode:vertical-rl;font-family:"Shippori Mincho B1",serif;font-weight:800;font-size:34px;
  line-height:1;color:var(--magenta);letter-spacing:2px;white-space:nowrap}
.item{position:absolute;width:340px}
.item .label{color:var(--white);font-weight:700;font-size:19px;white-space:nowrap}
.item .price{font-weight:900;font-size:64px;line-height:1;letter-spacing:-1px;
  background:linear-gradient(180deg,var(--gold-1) 0%,var(--gold-2) 55%,var(--gold-3) 100%);
  -webkit-background-clip:text;background-clip:text;color:transparent}
.item .price small{font-size:36px;letter-spacing:0}
.col-left{left:34px}
.col-right{left:500px}
.row1{top:92px}.row2{top:228px}.row3{top:362px}
.ribbon-band{position:absolute;left:0;top:490px;width:843px;height:170px}
.ribbon-deco{position:absolute;left:30px;top:540px;width:140px;height:70px;
  background:linear-gradient(135deg,#f3d58a,#d9a93a);border-radius:8px;opacity:.9}
.headline{position:absolute;left:0;top:530px;width:843px;text-align:center;color:var(--magenta-deep);line-height:1.2}
.headline .brand-name{font-family:"Shippori Mincho B1",serif;font-weight:800;font-size:72px}
.headline .no{font-family:"Shippori Mincho B1",serif;font-weight:700;font-size:52px}
.headline .script{font-family:"Yuji Syuku",serif;font-size:84px;color:var(--magenta)}
.festival{position:absolute;left:40px;top:690px;font-family:"Shippori Mincho B1",serif;font-weight:800;
  font-size:160px;line-height:1;color:var(--magenta);letter-spacing:-6px;white-space:nowrap}
.session{position:absolute;left:545px;top:690px;width:280px;text-align:center;color:var(--magenta-deep)}
.session .tag{display:inline-block;background:var(--magenta);color:var(--white);font-weight:700;font-size:26px;
  padding:4px 26px;border-radius:20px}
.session .date{font-weight:900;font-size:52px;line-height:1.1;white-space:nowrap}
.session .date small{font-size:28px}
.session .arrow{display:block;margin:2px auto}
.session .hours{font-weight:700;font-size:15px;color:var(--ink);margin-top:6px;white-space:nowrap}
.note{position:absolute;left:40px;top:950px;width:390px;font-size:15px;font-weight:700;color:var(--ink);line-height:1.6}
.venue{position:absolute;left:40px;top:1025px;font-weight:900;font-size:50px;line-height:1.2;color:var(--magenta-deep);white-space:nowrap}
.map{position:absolute;left:455px;top:940px;width:360px;height:172px;background:linear-gradient(135deg,#ffffff,#f3dbe5);
  border:2px solid var(--magenta)}
.address{position:absolute;left:40px;top:1116px;font-size:16px;font-weight:700;color:var(--ink);white-space:nowrap}
.organizer{position:absolute;left:0;top:1150px;width:843px;height:50px;background:var(--magenta);color:var(--white);
  font-size:16px;font-weight:700;display:flex;align-items:center;padding-left:30px;gap:18px;white-space:nowrap}
</style>
</head>
<body>
<div class="poster">
  <div class="flower-deco left" role="img" aria-label="ピンクの花の装飾"></div>
  <div class="flower-deco right" role="img" aria-label="ピンクの花の装飾"></div>

  <div class="brand"><div class="name">ROSALIE</div><div class="sub">Meiyou Co.,Ltd.</div></div>

  <div class="sale-band"><span>春物・夏物</span><span>特別特価</span></div>

  <div class="item col-left row1"><div class="label">シルクスカート・ネックカバー各種</div><div class="price">1,000<small>円~</small></div></div>
  <div class="item col-left row2"><div class="label">綿・テンセルTシャツ各種(日本製)</div><div class="price">2,900<small>円~</small></div></div>
  <div class="item col-left row3"><div class="label">チュニック各種(S~LL)</div><div class="price">2,900<small>円~</small></div></div>
  <div class="item col-right row1"><div class="label">カーディガン各種(日本製)</div><div class="price">4,900<small>円~</small></div></div>
  <div class="item col-right row2"><div class="label">パンツ各種(7号~9号)</div><div class="price">3,900<small>円~</small></div></div>
  <div class="item col-right row3"><div class="label">ジャケット各種(S~LL)</div><div class="price">5,900<small>円~</small></div></div>

  <svg class="ribbon-band" viewBox="0 0 843 170" preserveAspectRatio="none">
    <path d="M0 10 Q210 -10 421 10 T843 10 L843 160 Q630 180 421 160 T0 160 Z" fill="#fde6ef"/>
    <path d="M0 10 Q210 -10 421 10 T843 10" fill="none" stroke="#ffffff" stroke-width="6"/>
    <path d="M0 160 Q210 140 421 160 T843 160" fill="none" stroke="#ffffff" stroke-width="6"/>
  </svg>
  <div class="ribbon-deco" role="img" aria-label="金色のリボンの装飾"></div>
  <div class="headline"><span class="brand-name">明葉</span><span class="no">の</span><span class="script">婦人服</span></div>

  <div class="festival">春祭り</div>

  <div class="session">
    <span class="tag">会期</span>
    <div class="date">4月5日<small>(火)</small></div>
    <svg class="arrow" width="30" height="20" viewBox="0 0 30 20"><path d="M0 0 H30 L15 20 Z" fill="#c8236e"/></svg>
    <div class="date">4月10日<small>(日)</small></div>
    <div class="hours">10:00~18:00(最終日のみ15:00迄)</div>
  </div>

  <p class="note">今回もお値打ち品を多数取り揃えております!品質・価格に自信あり、ぜひお越し下さい。</p>
  <div class="venue">SPACEはなゆき</div>
  <div class="map" role="img" aria-label="会場周辺の地図"></div>

  <p class="address">アサギリモール一階・北側 京都市北区雲井南梅枝町38-6</p>
  <div class="organizer"><span>主催 株式会社明葉</span><span>京都市北区雲井西竹丘町17-42</span><span>tel075-555-0183</span><span>http://rosalie-fashion.jp/</span></div>
</div>
</body>
</html>
```